Flyer Tally Desk Ledger Kit

Hi
Can you please design me a DL Flyer for: Tally Desk Ledger Kit
Info:
Starting a new Business ?
Want to save on bookkeeping fees for your existing business?

You can now save 1000's off bookkeeping fees by Doing it Yourself.

Using our Bookkeeper software you simply key in the information as you go.

We offer one on one training, backup and support.
We can assist you with BAS Preparation and Payrol Advice.

Add Modules as required:
Point of Sale Module
Jobs Management Module
Website Intergration Module

Fee set up assistance and training.

Lets get the ball rolling: 1300 462 815
www.tldlk.com.au
admin@tldlk.com.au (use the logo thing you made)

Target Market(s)

Small Business

Colors
ec1f27
f04a50
f59296
fcdcdc
ffffff

Requirements
Nice to have
• image/s related to bookkeeping

```html
<!DOCTYPE html>
<html lang="en">
<head>
<meta charset="utf-8">
<title>Tally Desk Ledger Kit – Pull-up Banner</title>
<link href="https://fonts.googleapis.com/css2?family=Roboto:wght@400;500;700&display=swap" rel="stylesheet">
<style>
  :root {
    --red: #ec1f27;
    --coral: #f04a50;
    --rose: #f59296;
    --blush: #fcdcdc;
    --white: #ffffff;
    --ink: #555659;
    --stage: #e6e6e8;
  }
  * { margin: 0; padding: 0; box-sizing: border-box; }
  html, body {
    width: 1200px; height: 1175px; overflow: hidden;
    background: var(--stage);
    font-family: "Roboto", Arial, sans-serif;
    color: var(--ink);
  }
  .banner {
    position: absolute; left: 321px; top: 18px;
    width: 558px; height: 1139px;
    background: var(--white);
    border: 2px solid var(--rose);
    overflow: hidden;
  }
  .book {
    position: absolute; left: 37px; width: 485px;
    border-radius: 6px 40px 40px 6px;
  }
  .book-inner {
    position: absolute; left: 14px; right: 26px; top: 16px; bottom: 16px;
    display: flex; align-items: center; justify-content: center;
    text-align: center;
  }
  .book-logo { top: 15px; height: 146px; background: var(--blush); }
  .book-logo .book-inner { background: var(--white); left: 16px; }
  .book-start { top: 166px; height: 148px; background: var(--coral); }
  .book-start .book-inner { background: linear-gradient(90deg, var(--blush), var(--white) 45%, var(--blush)); }
  .book-save { top: 318px; height: 192px; background: var(--rose); }
  .book-save .book-inner { background: linear-gradient(90deg, var(--blush), var(--white) 40%, var(--white) 70%, var(--blush)); }

  .brand { display: flex; align-items: center; gap: 14px; }
  .brand-mark { width: 40px; height: 40px; border-radius: 50%; background: var(--red); }
  .brand-name { font-size: 34px; font-weight: 700; color: var(--red); letter-spacing: -0.5px; }

  .headline { font-size: 46px; font-weight: 700; line-height: 1.08; color: var(--ink); }
  .subhead { font-size: 35px; font-weight: 700; line-height: 1.18; color: var(--ink); }

  .offer {
    position: absolute; top: 532px; left: 0; width: 100%;
    text-align: center; font-size: 22px; line-height: 1.35;
  }
  .offer strong { color: var(--red); font-weight: 700; }

  .benefits { position: absolute; top: 606px; left: 40px; width: 470px; list-style: none; }
  .benefits li {
    display: flex; gap: 14px; font-size: 18px; line-height: 1.3; margin-bottom: 16px;
  }
  .benefits svg { flex: none; margin-top: 1px; }

  .modules-swoosh { position: absolute; left: 0; top: 760px; width: 558px; height: 245px; }
  .module-list { position: absolute; top: 0; left: 0; list-style: none; transform: rotate(-4deg); transform-origin: 60px 160px; }
  .module-list li { position: absolute; white-space: nowrap; font-size: 20px; }
  .module-list li::before { content: "• "; color: var(--red); }

  .contact { position: absolute; top: 1010px; left: 0; width: 100%; text-align: center; }
  .contact-lead { font-size: 25px; font-weight: 700; color: var(--ink); }
  .contact-phone { font-size: 45px; font-weight: 700; color: var(--red); margin-top: 2px; letter-spacing: 1px; }
  .contact-links { font-size: 23px; font-weight: 700; color: var(--red); margin-top: 4px; }
  .contact-links .dot { margin: 0 10px; }
</style>
</head>
<body>
<main class="banner">

  <section class="book book-logo">
    <div class="book-inner">
      <div class="brand">
        <span class="brand-mark"></span>
        <span class="brand-name">Tally Desk Ledger Kit</span>
      </div>
    </div>
  </section>

  <section class="book book-start">
    <div class="book-inner">
      <h1 class="headline">Starting a new<br>Business ?</h1>
    </div>
  </section>

  <section class="book book-save">
    <div class="book-inner">
      <h2 class="subhead">Want to save on<br>bookkeeping fees for<br>your existing business?</h2>
    </div>
  </section>

  <p class="offer">You can now <strong>SAVE 1000's OFF</strong><br>bookkeeping fees by Doing it Yourself</p>

  <ul class="benefits">
    <li><svg width="30" height="20" viewBox="0 0 30 20"><path d="M2 7h16V2l10 8-10 8v-5H2z" fill="none" stroke="#ec1f27" stroke-width="2" stroke-linejoin="round"/></svg><span>Using our Bookkeeper software you simply<br>key in the information as you go</span></li>
    <li><svg width="30" height="20" viewBox="0 0 30 20"><path d="M2 7h16V2l10 8-10 8v-5H2z" fill="none" stroke="#ec1f27" stroke-width="2" stroke-linejoin="round"/></svg><span>We offer one on one training, backup and support</span></li>
    <li><svg width="30" height="20" viewBox="0 0 30 20"><path d="M2 7h16V2l10 8-10 8v-5H2z" fill="none" stroke="#ec1f27" stroke-width="2" stroke-linejoin="round"/></svg><span>We can assist you with BAS Preparation and<br>Payrol Advice</span></li>
  </ul>

  <section class="modules-swoosh">
    <svg width="558" height="245" viewBox="0 0 558 245">
      <path d="M0 88 C200 80 400 40 558 8 L558 205 C380 235 200 230 0 218 Z" fill="#fcdcdc"/>
      <path d="M0 78 C210 74 400 38 558 0 L558 14 C400 62 240 108 0 112 Z" fill="#ec1f27"/>
      <path d="M0 212 C200 232 400 210 558 168 L558 184 C400 232 200 246 0 232 Z" fill="#ec1f27"/>
      <text x="38" y="60" transform="rotate(-6 38 60)" font-family="Roboto, Arial, sans-serif" font-size="24" font-weight="700" fill="#f04a50">Fee Set up Assistance and Training</text>
      <text x="40" y="102" transform="rotate(-4 40 102)" font-family="Roboto, Arial, sans-serif" font-size="20" font-weight="500" fill="#ffffff">Add Modules as Required</text>
    </svg>
    <ul class="module-list">
      <li style="left:56px; top:130px;">Point of Sale Module</li>
      <li style="left:68px; top:158px;">Jobs Management Module</li>
      <li style="left:80px; top:186px;">Website Intergration Module</li>
    </ul>
  </section>

  <footer class="contact">
    <p class="contact-lead">Lets Get the Ball Rolling:</p>
    <p class="contact-phone">1300 462 815</p>
    <p class="contact-links">www.tldlk.com.au<span class="dot">•</span>admin@tldlk.com.au</p>
  </footer>

</main>
</body>
</html>
```